Lumo.app Homepage Redesign

We are seeking a talented designer to create an emotive and aspirational homepage for our website (www.lumo.app) that elevates the Lumo.app brand using our new home page copy.

Our current design feels product-heavy and lacks the global, professional, and emotive touch we're aiming for.

We want to strip back unnecessary visual distractions and focus on a more streamlined, compelling design that resonates with our audience.

Project Goals:
Replace product-heavy, literal imagery with more evocative, aspirational visuals.
Create a homepage that feels aspirational and professional, reflecting our global ambitions.
Explore the use of icons or simple graphics to reduce visual clutter and create a more refined experience.
Ensure that usability principles are at the forefront of the design. Navigation must be clear and accessible on both desktop and mobile.
Practicality is key. Any animations or transitions should serve a functional purpose and should not hinder website speed or performance.
We prefer mockups in Adobe XD for ease of use by our developer, but Photoshop is also acceptable if this suits your workflow better.

Design Considerations:
Imagery: The selected imagery should enhance the emotive feel of the site, not simply fill space.
Usability: Avoid hidden navigation on desktop, and ensure key call-to-action buttons like "Watch Demo" and "Book a Demo" are clearly identifiable as clickable.
Animations/Transitions: Any animated elements should focus on showcasing our content, not just adding visual flair. Consider website performance and practicality in your design.
Content Hierarchy: Follow the suggested hierarchy based on provided copy, giving prominence to our key propositions while minimizing distractions.
Style: Maintain Lumo.app's colour scheme and font set, but we welcome fresh perspectives on how to apply them.
Copy: We will be providing new written copy to replace the current content on the website. The new design should complement and elevate the revised messaging.

Deliverables:
An initial homepage mock-up based on our brand guidelines.
Two rounds of feedback and revisions based on our input.
Final design files provided in Adobe XD (preferred) or Photoshop.

Brand Resources:
You will be given access to our Adobe Library, Brand Guidelines, and new website copy (and indicative wireframe), along with any necessary imagery from our stock library.
Note: please contact us if you would like access to our Adobe Library.

Number of Pages Required

1 page

Font styles to use
Sans Serif
Other font styles liked:
• Poppins Bold, Proxima Nova Light, Bold.

Colors

Designer to choose colors to be used in the design.

Requirements
Must have
• New website copy as supplied and ideally follow the wireframe provided. Aspirational visuals. Meets our brand guidelines
Should not have
• Stock standard imagery.

```html
<!DOCTYPE html>
<html lang="en">
<head>
<meta charset="utf-8">
<title>Lumo.app — Reach The Unreachable</title>
<link rel="stylesheet" href="https://fonts.googleapis.com/css2?family=Poppins:wght@300;400;500;600;700;800&display=swap">
<style>
:root{
  --red:#e42d23;
  --red-dark:#c91d16;
  --ink:#1d1d1f;
  --text:#555a60;
  --muted:#8a8f95;
  --line:#e6e6e8;
  --soft:#f3f3f4;
  --white:#fff;
}
*{box-sizing:border-box;margin:0;padding:0}
html,body{width:1200px;height:4231px;overflow:hidden}
body{position:relative;background:var(--white);font-family:"Poppins",sans-serif;color:var(--ink)}
.abs{position:absolute}
.red{color:var(--red)}
.btn{position:absolute;display:flex;align-items:center;justify-content:center;border-radius:30px;font-size:10px;font-weight:700;letter-spacing:.2px;text-transform:uppercase;height:38px}
.btn-red{background:var(--red);color:#fff}
.btn-dark{background:var(--ink);color:#fff}
.btn-white{background:#fff;color:var(--ink)}
.btn-outline{border:1.5px solid var(--ink);color:var(--ink);background:#fff}
.btn-outline-white{border:1.5px solid #fff;color:#fff}
.brand{font-weight:800;color:var(--red);letter-spacing:-1.5px}
.photo{position:absolute}

/* header */
.topbar{left:690px;top:0;width:410px;height:28px;background:var(--red);border-radius:0 0 0 14px;color:#fff;font-size:9px;font-weight:600;display:flex;align-items:center;gap:22px;padding-left:22px}
.topbar .tools{margin-left:auto;display:flex;gap:22px;padding-right:18px}
.nav{top:52px;left:590px;display:flex;gap:30px;font-size:11px;font-weight:500;align-items:center}
.nav .demo{border:1.5px solid var(--ink);border-radius:20px;padding:8px 16px;font-size:9px;font-weight:700}

/* hero */
.hero-title{left:122px;top:232px;font-size:104px;font-weight:800;color:var(--red);line-height:1;letter-spacing:-2px}
.hero-sub{left:124px;top:332px;font-size:42px;font-weight:400;letter-spacing:-.5px}
.hero-copy{left:125px;top:388px;width:330px;font-size:15px;line-height:22px;color:var(--ink)}
.hero-cta{left:125px;top:448px;font-size:21px;font-weight:700;border-bottom:2px solid var(--ink);padding-bottom:2px}
.hero-small{left:125px;top:504px;width:440px;font-size:11px;line-height:16px;color:var(--text)}
.card{position:absolute;background:#fff;border-radius:12px;box-shadow:0 8px 28px rgba(0,0,0,.12)}
.stat-label{font-size:8px;color:var(--muted)}
.stat-val{font-size:20px;font-weight:600;display:flex;align-items:center;gap:10px}
.chip{font-size:8px;color:#2a9a57;background:#e5f6ec;border-radius:10px;padding:1px 7px;font-weight:500}

.section-title{width:100%;text-align:center;font-size:29px;font-weight:600;line-height:36px}
.section-lead{width:100%;text-align:center;font-size:11px;color:var(--text)}

/* features */
.features{top:1282px;left:180px;width:850px;display:flex;justify-content:space-between}
.feature{width:110px;text-align:center;font-size:9px;font-weight:600;line-height:12px}
.feature svg{display:block;margin:0 auto 8px;width:38px;height:38px}

.h3{font-size:23px;font-weight:600}
.para{font-size:11px;line-height:17px;color:var(--text)}

/* red band */
.band{left:0;top:1785px;width:1200px;height:489px;background:linear-gradient(120deg,#e8352b,#d42219);border-radius:24px;overflow:hidden}

/* logos */
.partner{position:absolute;border-radius:50%}

/* teams */
.team-item{position:absolute;display:flex;align-items:center;gap:16px;font-size:13px;font-weight:600;line-height:18px}
.team-ico{width:40px;height:40px;border-radius:50%;background:var(--soft);display:flex;align-items:center;justify-content:center}

/* footer */
.fcol h4{font-size:15px;font-weight:600;margin-bottom:11px}
.fcol li{list-style:none;font-size:9.5px;color:var(--muted);line-height:19px}
.social{position:absolute;top:4014px;width:38px;height:38px;border-radius:50%}
</style>
</head>
<body>

<!-- Header -->
<div class="abs brand" style="left:124px;top:20px;font-size:48px">Lumo.app</div>
<div class="abs topbar">
  <span>✉ Become a Partner</span><span>☏ Contact us</span>
  <span class="tools"><span>●▾</span><span>▢</span><span>○</span></span>
</div>
<nav class="abs nav">
  <span><span class="red">⌂</span>&nbsp; Platform ▾</span><span>Solutions ▾</span><span>Resources</span><span>About</span><span>Pricing</span><span class="demo">BOOK A DEMO</span>
</nav>

<!-- Hero -->
<svg class="abs" style="left:0;top:94px" width="1200" height="570" viewBox="0 0 1200 570">
  <defs>
    <linearGradient id="heroRed" x1="0" y1="0" x2="1" y2="1"><stop offset="0" stop-color="#ef3a2f"/><stop offset="1" stop-color="#c81a12"/></linearGradient>
    <radialGradient id="heroFade" cx="0.1" cy="0.2" r="0.6"><stop offset="0" stop-color="#fbe3e1"/><stop offset="1" stop-color="#fff" stop-opacity="0"/></radialGradient>
  </defs>
  <rect width="1200" height="570" fill="url(#heroFade)"/>
  <path d="M560 0 H1200 V430 C1120 520 980 580 820 550 C660 520 560 440 530 320 C505 210 520 80 560 0Z" fill="url(#heroRed)"/>
  <path d="M640 0 C720 120 900 200 1200 180" stroke="#fff" stroke-opacity=".18" stroke-width="2" fill="none"/>
  <path d="M600 60 C700 240 920 300 1200 260" stroke="#fff" stroke-opacity=".12" stroke-width="2" fill="none"/>
</svg>
<div class="photo" role="img" aria-label="Smiling young man in glasses and denim shirt working on a laptop" style="left:650px;top:100px;width:400px;height:545px;border-radius:200px 200px 40px 40px;background:linear-gradient(180deg,rgba(240,200,170,.55),rgba(120,160,210,.65) 60%,rgba(90,100,120,.55))"></div>

<div class="abs hero-title">Reach</div>
<div class="abs hero-sub">The Unreachable.|</div>
<p class="abs hero-copy">You know you have a problem. We know why you have a problem.</p>
<div class="abs hero-cta">Let’s solve it together</div>
<p class="abs hero-small">You’re not here by accident. You’re also not alone. Many large, complex businesses are facing the same communication challenges <b class="red">MORE..</b></p>

<div class="card" style="left:673px;top:235px;width:153px;height:164px;padding:10px">
  <div style="font-size:6px;font-weight:600">Average review rating</div>
  <div style="font-size:5px;color:var(--muted)">Overall rating across all staff</div>
  <svg width="133" height="120" viewBox="0 0 133 120" style="margin-top:6px">
    <g fill="#e42d23">
      <rect x="4" y="40" width="7" height="70"/><rect x="16" y="20" width="7" height="90"/><rect x="28" y="50" width="7" height="60"/><rect x="40" y="28" width="7" height="82"/><rect x="52" y="45" width="7" height="65"/><rect x="64" y="15" width="7" height="95"/><rect x="76" y="38" width="7" height="72"/><rect x="88" y="25" width="7" height="85"/><rect x="100" y="48" width="7" height="62"/><rect x="112" y="30" width="7" height="80"/>
    </g>
    <g fill="#f7c7c3"><rect x="4" y="10" width="7" height="30"/><rect x="28" y="14" width="7" height="36"/><rect x="52" y="12" width="7" height="33"/><rect x="76" y="8" width="7" height="30"/><rect x="100" y="10" width="7" height="38"/></g>
  </svg>
</div>
<div class="card" style="left:1113px;top:235px;width:100px;height:105px;padding:8px">
  <div style="font-size:6px;font-weight:600">Active now</div>
  <svg width="70" height="70" viewBox="0 0 70 70" style="margin:6px 0 0 4px">
    <circle cx="35" cy="35" r="28" fill="none" stroke="#f8d3d0" stroke-width="6"/>
    <circle cx="35" cy="35" r="28" fill="none" stroke="#e42d23" stroke-width="6" stroke-dasharray="140 176" transform="rotate(-90 35 35)"/>
    <text x="35" y="38" font-size="9" font-weight="700" text-anchor="middle" fill="#1d1d1f" font-family="Poppins, sans-serif">316</text>
  </svg>
</div>
<div class="card" style="left:673px;top:512px;width:222px;height:133px;padding:10px">
  <div style="display:flex;justify-content:space-between;font-size:5px;color:var(--muted)"><span>● Last week &nbsp; ● This week</span><span>Daily · Weekly · Month</span></div>
  <div style="font-size:6px;font-weight:600;margin:8px 0 0 88px">May 2023</div>
  <svg width="200" height="85" viewBox="0 0 200 85">
    <path d="M0 70 C30 72 45 30 60 55 C75 80 90 82 110 60 C130 38 140 10 160 30 C175 45 190 40 200 20 V85 H0Z" fill="#fde5e3"/>
    <path d="M0 70 C30 72 45 30 60 55 C75 80 90 82 110 60 C130 38 140 10 160 30 C175 45 190 40 200 20" stroke="#e42d23" stroke-width="2" fill="none"/>
  </svg>
</div>
<div class="card" style="left:998px;top:506px;width:164px;height:170px;padding:14px 14px">
  <div class="stat-label">Total members</div>
  <div class="stat-val">4,862 <span class="chip">+ 9.2%</span></div>
  <div class="stat-label" style="margin-top:12px">Paid members</div>
  <div class="stat-val">2,671 <span class="chip">+ 6.6%</span></div>
  <div class="stat-label" style="margin-top:12px">Email open rate</div>
  <div class="stat-val">82% <span class="chip">+ 8.1%</span></div>
</div>

<!-- Bridge section -->
<svg class="abs" style="left:0;top:738px" width="1200" height="480" viewBox="0 0 1200 480">
  <path d="M0 80 C40 20 130 0 200 40 L330 150 C380 200 380 260 330 310 L200 430 C150 480 70 480 0 450Z" fill="#efefef"/>
  <path d="M1200 120 C1050 150 1020 300 1090 380 C1130 420 1170 430 1200 430" stroke="#f2c9c6" stroke-width="1.5" fill="none"/>
  <path d="M1200 90 C1030 130 1000 300 1075 395 C1115 440 1170 450 1200 450" stroke="#f2c9c6" stroke-width="1" fill="none"/>
</svg>
<h2 class="abs section-title" style="top:694px">Lumo Bridge The <span class="red">Communication Gap</span><br>In Your Workplace</h2>
<p class="abs section-lead" style="top:783px">Empower your team with seamless communication to create a more informed, aligned, and inspired work environment.</p>
<div class="photo" role="img" aria-label="Desktop monitors, a laptop, tablet and phone showing workplace comms screens" style="left:287px;top:829px;width:624px;height:222px;border-radius:8px;background:linear-gradient(100deg,#2b2f3a 0%,#4a5a6b 35%,#d8dadd 50%,#3a2327 70%,#8e1c17 100%)"></div>
<div class="btn btn-red" style="left:425px;top:1092px;width:170px">Book a Demo</div>
<div class="btn btn-dark" style="left:606px;top:1092px;width:168px">Watch Video &nbsp;<span style="display:inline-flex;width:16px;height:16px;border-radius:50%;background:#555;align-items:center;justify-content:center;font-size:7px">▶</span></div>
<div class="abs" style="left:606px;top:1137px;width:168px;text-align:center;font-size:10px;font-style:italic;font-weight:500">Duration (4:40)</div>

<!-- Emotive Feature -->
<h2 class="abs section-title" style="top:1222px"><span class="red">Emotive</span> Feature</h2>
<div class="abs features">
  <div class="feature"><svg viewBox="0 0 38 38" fill="none" stroke="#333" stroke-width="1.4"><circle cx="19" cy="12" r="8"/><path d="M8 34 V24 H30 V34 M13 24 V34 M25 24 V34"/></svg>Manage the<br>Culture</div>
  <div class="feature"><svg viewBox="0 0 38 38" fill="none" stroke="#333" stroke-width="1.4"><circle cx="19" cy="19" r="13"/><path d="M14 15 V23 L20 26 V12Z M24 15 Q27 19 24 23"/></svg>Calm the<br>Noise</div>
  <div class="feature"><svg viewBox="0 0 38 38" fill="none" stroke="#333" stroke-width="1.4"><circle cx="17" cy="14" r="9"/><path d="M12 34 L14 24 M22 24 L24 34 M24 6 L30 3"/></svg>Change<br>Behaviour</div>
  <div class="feature"><svg viewBox="0 0 38 38" fill="none" stroke="#e42d23" stroke-width="1.4"><path d="M19 7 A9 9 0 0 1 24 24 V28 H14 V24 A9 9 0 0 1 19 7Z M15 32 H23 M19 2 V4 M6 10 L8 11 M32 10 L30 11"/></svg><span class="red">Inspire &amp;<br>Excite</span></div>
  <div class="feature"><svg viewBox="0 0 38 38" fill="none" stroke="#333" stroke-width="1.4"><circle cx="19" cy="12" r="5"/><path d="M11 34 V24 Q19 18 27 24 V34 M4 20 L11 26 M34 20 L27 26"/></svg>Empower<br>Teams</div>
  <div class="feature"><svg viewBox="0 0 38 38" fill="none" stroke="#333" stroke-width="1.4"><circle cx="19" cy="7" r="3"/><circle cx="8" cy="24" r="3"/><circle cx="19" cy="24" r="3"/><circle cx="30" cy="24" r="3"/><path d="M19 10 V18 M8 21 V17 H30 V21 M4 34 V30 H12 V34 M15 34 V30 H23 V34 M26 34 V30 H34 V34"/></svg>Organisational<br>Glue</div>
  <div class="feature"><svg viewBox="0 0 38 38" fill="none" stroke="#333" stroke-width="1.4"><circle cx="19" cy="19" r="13"/><circle cx="19" cy="19" r="6"/><path d="M19 2 V8 M19 30 V36 M2 19 H8 M30 19 H36"/></svg>Unify the<br>Workplace</div>
  <div class="feature"><svg viewBox="0 0 38 38" fill="none" stroke="#333" stroke-width="1.4"><circle cx="19" cy="8" r="4"/><path d="M12 20 Q19 13 26 20 M6 26 H32 V32 H6Z M19 26 V20"/></svg>Frontline to<br>Backoffice</div>
</div>
<div class="abs" style="left:0;top:1378px;width:1200px;height:1px;background:var(--line)"></div>
<div class="abs" style="left:509px;top:1375px;width:83px;height:3px;background:var(--red)"></div>

<!-- Inspire & Excite -->
<svg class="abs" style="left:420px;top:1460px" width="290" height="290" viewBox="0 0 290 290"><circle cx="145" cy="145" r="130" fill="none" stroke="#f2f2f3" stroke-width="36"/></svg>
<div class="photo" role="img" aria-label="Smiling young woman in a straw hat looking at her phone" style="left:330px;top:1420px;width:330px;height:362px;border-radius:165px 165px 0 0;background:linear-gradient(180deg,#e8d5b8 0%,#f2d9c6 45%,#d9d9dc 100%)"></div>
<div class="partner" style="left:536px;top:1493px;width:30px;height:30px;background:#fff;box-shadow:0 3px 10px rgba(0,0,0,.12)"></div>
<div class="partner" style="left:605px;top:1512px;width:28px;height:28px;background:#fff;box-shadow:0 3px 10px rgba(0,0,0,.12)"></div>
<div class="partner" style="left:619px;top:1578px;width:34px;height:34px;background:#fff;box-shadow:0 3px 10px rgba(0,0,0,.12)"></div>
<div class="partner" style="left:565px;top:1622px;width:30px;height:30px;background:#fff;box-shadow:0 3px 10px rgba(0,0,0,.12)"></div>
<div class="card" style="left:208px;top:1548px;width:194px;height:168px;padding:14px 14px;border-radius:6px">
  <div style="font-size:12px;font-weight:600">PR Views</div>
  <svg width="170" height="120" viewBox="0 0 170 120" style="margin-top:6px">
    <g font-size="7" fill="#555" font-family="Poppins, sans-serif"><text x="0" y="18">10K</text><text x="0" y="42">05K</text><text x="0" y="66">2.5K</text><text x="0" y="90">01K</text></g>
    <g fill="#d7dcec"><rect x="28" y="55" width="8" height="40"/><rect x="44" y="45" width="8" height="50"/><rect x="60" y="60" width="8" height="35"/><rect x="76" y="50" width="8" height="45"/><rect x="92" y="40" width="8" height="55"/><rect x="124" y="50" width="8" height="45"/><rect x="140" y="45" width="8" height="50"/></g>
    <rect x="108" y="30" width="9" height="65" fill="#e42d23"/>
    <rect x="98" y="10" width="30" height="13" rx="2" fill="#e42d23"/><text x="113" y="19" font-size="7" fill="#fff" text-anchor="middle" font-family="Poppins, sans-serif">5,290</text>
    <g font-size="7" fill="#333" font-family="Poppins, sans-serif"><text x="26" y="108">10</text><text x="42" y="108">11</text><text x="58" y="108">12</text><text x="74" y="108">13</text><text x="90" y="108">14</text><text x="106" y="108">15</text><text x="122" y="108">16</text><text x="138" y="108">17</text><text x="154" y="108">18</text></g>
  </svg>
</div>
<div class="abs h3" style="left:713px;top:1494px">Inspire &amp; Excite</div>
<p class="abs para" style="left:714px;top:1535px;width:280px">Ever felt uplifted by an email blast? Or inspired by a text message?</p>
<p class="abs para" style="left:714px;top:1582px;width:280px">Using vibrant visuals to deliver timely and engaging screen content, you can generate excitement and motivate your workforce.</p>
<div class="btn btn-red" style="left:714px;top:1652px;width:118px;height:34px">Book a Demo</div>

<!-- Red band -->
<div class="abs band">
  <h3 class="abs" style="left:0;top:26px;width:1200px;text-align:center;color:#fff;font-size:18px;font-weight:600;line-height:28px">Lumo Is The One Workplace Comms Platform That<br>Reaches &amp; Engages Everyone,Everywhere.</h3>
  <div class="abs" style="left:0;top:105px;width:1200px;height:1px;background:rgba(255,255,255,.35)"></div>
  <div class="abs" style="left:595px;top:150px;width:415px;height:265px;background:rgba(255,255,255,.18);border-radius:14px;transform:rotate(-3deg)"></div>
  <div class="abs" style="left:196px;top:200px;color:#fff;font-size:29px;font-weight:700;line-height:32px">Transform How You<br>Connect</div>
  <div class="abs" style="left:196px;top:274px;color:#fff;font-size:11px;font-weight:700">With Hard-To-Reach Workers.</div>
  <p class="abs" style="left:196px;top:303px;width:330px;color:#fff;font-size:11px;line-height:16px">Lumo brings together digital workplace screens,  desktops and mobiles to reach all your people – whether they’re at home at their desks, on the roador the factory floor.</p>
  <div class="btn btn-white" style="left:196px;top:370px;width:116px;height:34px">Book a Demo</div>
  <div class="photo" role="img" aria-label="Excited young woman in glasses holding a phone beside a mobile app screen" style="left:610px;top:140px;width:390px;height:300px;border-radius:150px 150px 10px 10px;background:linear-gradient(180deg,rgba(255,230,215,.75),rgba(245,220,205,.55) 55%,rgba(255,255,255,.25))"></div>
  <div class="abs" style="left:860px;top:218px;width:114px;height:106px;background:#fff;border-radius:4px;box-shadow:0 4px 14px rgba(0,0,0,.15);font-size:8.5px;color:#333;padding:6px 8px;line-height:21px">
    <div style="font-style:italic">None</div><div>Web Portal</div><div style="background:#eef0f5">File Upload (XLSX)</div><div>Cloud Sheets</div><div>TeamDrive (XLSX)</div>
  </div>
  <svg class="abs" style="left:680px;top:310px" width="300" height="80"><path d="M40 60 H200 V10" stroke="#fff" stroke-dasharray="4 4" stroke-width="1.5" fill="none"/></svg>
</div>

<!-- Large businesses -->
<h2 class="abs section-title" style="top:2327px;font-size:23px;line-height:29px">Lumo Works For Large, <span class="red">Complex Businesses</span><br>And It Will Work For You, Too</h2>
<svg class="abs" style="left:180px;top:2420px" width="420" height="420" viewBox="0 0 420 420">
  <path d="M110 55 A190 190 0 0 0 40 260" stroke="#1d1d1f" stroke-width="1.5" fill="none"/>
  <path d="M370 230 A190 190 0 0 1 170 395" stroke="#1d1d1f" stroke-width="1.5" fill="none"/>
  <path d="M270 40 A190 190 0 0 1 370 150" stroke="#1d1d1f" stroke-width="1.5" fill="none"/>
  <path d="M120 100 A130 130 0 0 0 90 200" stroke="#1d1d1f" stroke-width="1.5" fill="none"/>
  <path d="M300 280 A130 130 0 0 1 240 330" stroke="#1d1d1f" stroke-width="1.5" fill="none"/>
  <circle cx="110" cy="55" r="4" fill="#1d1d1f"/><circle cx="370" cy="230" r="4" fill="#1d1d1f"/><circle cx="120" cy="100" r="3" fill="#1d1d1f"/><circle cx="300" cy="280" r="3" fill="#1d1d1f"/>
</svg>
<div class="partner" role="img" aria-label="Partner badge" style="left:354px;top:2410px;width:96px;height:96px;background:#1f6b35"></div>
<div class="partner" role="img" aria-label="Partner badge" style="left:544px;top:2527px;width:68px;height:68px;background:#f7cc14"></div>
<div class="partner" role="img" aria-label="Partner badge" style="left:189px;top:2583px;width:88px;height:88px;background:#e8432f"></div>
<div class="partner" role="img" aria-label="Partner badge" style="left:268px;top:2729px;width:108px;height:108px;background:#1b63c5"></div>
<div class="partner" role="img" aria-label="Partner badge" style="left:457px;top:2742px;width:80px;height:80px;background:#e4e6e8"></div>
<div class="abs brand" style="left:300px;top:2590px;font-size:50px">Lumo.app</div>

<div class="abs" style="left:668px;top:2510px;font-size:25px;font-weight:600;line-height:29px">We Can Easily Share<br>Information</div>
<div class="abs" style="left:668px;top:2578px;font-size:11px;font-weight:600;line-height:15px">To Staff Across New Zealand That Isn’t<br>Always Available To Them.</div>
<p class="abs para" style="left:668px;top:2623px;width:335px;font-size:10.5px;line-height:15px">The different templates are a bonus – there’s always a layout that works with what you need to share.</p>
<div class="btn btn-red" style="left:670px;top:2679px;width:116px;height:36px">Book a Demo</div>
<div class="btn btn-outline" style="left:795px;top:2679px;width:116px;height:36px">Free Trial</div>

<!-- Key teams -->
<h2 class="abs section-title" style="top:2896px">A Single Platform For All Your <span class="red">Key Teams</span></h2>
<div class="abs" style="left:171px;top:2972px;width:407px;height:153px;background:var(--soft);border-radius:14px;padding:24px 34px">
  <div style="display:flex;align-items:center;gap:14px">
    <svg width="40" height="36" viewBox="0 0 40 36" fill="none" stroke="#e42d23" stroke-width="1.3"><rect x="2" y="2" width="36" height="24" rx="2"/><circle cx="12" cy="14" r="4"/><circle cx="28" cy="14" r="4"/><path d="M12 26 V34 M28 26 V34 M6 34 H34 M18 10 H22"/></svg>
    <div style="font-size:13px;font-weight:600;line-height:18px">Lumo Works For Internal<br>Commmunications Teams</div>
  </div>
  <p class="para" style="font-size:10.5px;line-height:15px;margin-top:16px">Always pushed for time, often stretched for resources and people – Lumo takes a huge load off.</p>
  <div style="font-size:9px;font-weight:700;color:var(--red);margin-top:12px">READ MORE &nbsp;↗</div>
</div>
<div class="team-item" style="left:179px;top:3162px"><span class="team-ico"><svg width="24" height="24" viewBox="0 0 24 24" fill="none" stroke="#333" stroke-width="1.2"><rect x="2" y="3" width="20" height="14"/><path d="M6 13 L10 8 L14 11 L18 6 M8 21 H16 M12 17 V21"/></svg></span>No Need To Play Graphic<br>Designer</div>
<div class="team-item" style="left:179px;top:3248px"><span class="team-ico"><svg width="24" height="24" viewBox="0 0 24 24" fill="none" stroke="#333" stroke-width="1.2"><circle cx="12" cy="6" r="3"/><rect x="4" y="11" width="16" height="11"/><path d="M8 15 H16 M8 18 H14"/></svg></span>Bite-Sized Content For Snackable<br>Learning.</div>
<div class="photo" role="img" aria-label="Hands using a laptop showing a team photo with the message Take time out to interact and share" style="left:616px;top:2965px;width:405px;height:340px;border-radius:22px;background:linear-gradient(135deg,#e67a2a 0%,#c9542a 40%,#3c4a5e 70%,#9aa7b8 100%)"></div>

<!-- CTA -->
<svg class="abs" style="left:0;top:3396px" width="1200" height="460" viewBox="0 0 1200 460">
  <defs><linearGradient id="ctaRed" x1="0" y1="0" x2="1" y2="1"><stop offset="0" stop-color="#e8352b"/><stop offset="1" stop-color="#cf1f16"/></linearGradient></defs>
  <path d="M0 0 H1200 V330 C1000 470 700 450 420 380 C250 340 100 360 0 400Z" fill="url(#ctaRed)"/>
  <path d="M0 400 C100 360 250 340 420 380 C700 450 1000 470 1200 330 V345 C1000 480 700 465 420 395 C250 355 100 375 0 415Z" fill="#f0f0f0"/>
  <path d="M0 30 C300 80 500 20 1200 40" stroke="#fff" stroke-opacity=".1" stroke-width="2" fill="none"/>
</svg>
<h2 class="abs" style="left:0;top:3508px;width:1200px;text-align:center;color:#fff;font-size:29px;font-weight:700;line-height:37px">Transform The Way You Talk<br>To Your Workforce.</h2>
<p class="abs" style="left:0;top:3595px;width:1200px;text-align:center;color:#fff;font-size:19px">Lumo Will Enable You To Reach &amp; Engage Everyone, Everywhere.</p>
<div class="btn btn-white" style="left:479px;top:3644px;width:117px;height:36px">Book a Demo</div>
<div class="btn btn-outline-white" style="left:604px;top:3644px;width:116px;height:36px">Find Out More</div>

<!-- Footer -->
<div class="abs brand" style="left:126px;top:3930px;font-size:60px">Lumo.app</div>
<div class="social" role="img" aria-label="Social profile" style="left:178px;background:var(--ink)"></div>
<div class="social" role="img" aria-label="Social profile" style="left:222px;background:var(--red)"></div>
<div class="social" role="img" aria-label="Social profile" style="left:268px;background:var(--ink)"></div>
<div class="abs fcol" style="left:418px;top:3900px"><h4>Lumo.app</h4><ul><li>Platform Overview</li><li>Features</li><li>Security</li><li>Workplace Digital Signage Screens</li><li>Corporate Screensavers</li><li>Template Library</li><li>Integrations</li><li>Infotainment Streams</li><li>Premium Programs</li></ul></div>
<div class="abs fcol" style="left:629px;top:3900px"><h4>Who We’re For</h4><ul><li>Industrial &amp; Manufacturing</li><li>Mining &amp; Construction</li><li>Government &amp; Public Sector</li><li>Aged Care</li><li>Logistics</li><li>Retail</li></ul></div>
<div class="abs fcol" style="left:804px;top:3900px"><h4>Resources</h4><ul><li>Latest Insights</li><li>Snackable Learning Framework</li><li>Help Centre</li><li>Server Status</li><li>Privacy Policy</li><li>Terms &amp; Service</li></ul></div>
<div class="abs fcol" style="left:985px;top:3900px"><h4>Get Started</h4><ul><li>Book a Demo</li><li>Free Trial</li><li>Pricing</li><li>Become a Partner</li><li>Contact Us</li></ul></div>
<div class="abs" style="left:500px;top:4161px;font-size:9px;color:var(--muted)">© 2024 Lumo.app Limited All rights reserved</div>
<div class="abs" style="left:775px;top:4146px;width:300px;height:40px;border-radius:20px;background:#f2f2f3;display:flex;align-items:center;overflow:hidden">
  <span style="flex:1;padding-left:22px;font-size:9px;color:var(--muted)">Need help?</span>
  <span style="background:var(--red);color:#fff;height:100%;width:95px;display:flex;align-items:center;justify-content:center;font-size:9px;font-weight:700;border-radius:0 20px 20px 0">CHAT NOW</span>
</div>
<div class="abs" style="left:1124px;top:4144px;width:42px;height:42px;border-radius:50%;background:var(--ink);color:#fff;display:flex;align-items:center;justify-content:center;font-size:14px">⌃</div>

</body>
</html>
```